Plakate für Anbieter von Karosserie-Reparaturen und -Services
Zielgruppe
Unser Kunde, die Lindauer & Brack AG aus Oberbuchsiten (CH), ist ein Anbieter von Karosserie Reparaturen und Services. Er wird an einem öffentlichen Event teilnehmen und benötigt hierfür ein Plakat um seine Aktivität auf seinem Stand zu bewerben. Diese Aktivität ist für die Besucher die Teilnahme als Fahrer auf der Velotta-Rennbahn auf dem Stand. Hierfür benötigen wir ein Plakat (Format A0, farbig) welches auf das Rennen und die zu gewinneneden Preise aufmerksam macht.
Aufgabenstellung
Das Plakat muss modern, ansprechend, einladend und motivierend sein. Es kann mit Bilder (Vorschläge aus Lumexa-Stock) und Farben gearbeiten werden. Die Farben müssen nicht zwingend einen direkten Bezug zum Logo haben.
Dieser Text muss zwingend ersichtlich sein:
→ 15 Runden sind zu fahren
→ die schnellste Zeit gewinnt
Zu gewinnen gibt es
1. Preis: Gutschein im Wert von CHF 1'000.- von Vandermark
2. Preis: Fahrzeugreinigung inkl. Politur im Wert von CHF 800.-
3. Preis Werkstatt-Gutschein im Wert von CHF 400.-
Nebst dem Text benötigt es noch einen 'Call to Action' > z.B. Jetzt mitmachen und gewinne oder so ähnlich. Zudem benötigst es noch einen Platzhalter für ein zweites Logo. Dieses ist aktuell noch nicht definiert und wird dann erst bei der Finalisierung eingefügt.

```html
<!DOCTYPE html>
<html lang="de">
<head>
<meta charset="utf-8">
<title>Plakat – Carrosserie Lindauer + Brack</title>
<link href="https://fonts.googleapis.com/css2?family=Bebas+Neue&family=Roboto+Condensed:wght@400;500&display=swap" rel="stylesheet">
<style>
  :root {
    --brand-blue: #1f67a5;
    --charcoal: #333333;
    --white: #ffffff;
    --prize-orange: #f5a623;
    --page-bg: #ececec;
  }
  html, body {
    margin: 0;
    width: 1200px;
    height: 1096px;
    overflow: hidden;
    background: var(--page-bg);
  }
  .poster {
    position: absolute;
    left: 210px;
    top: 27px;
    width: 780px;
    height: 1041px;
    box-shadow: 0 2px 8px rgba(0,0,0,0.2);
  }
  .poster svg { display: block; width: 100%; height: 100%; }
  .display { font-family: 'Bebas Neue', sans-serif; }
  .body-text { font-family: 'Roboto Condensed', sans-serif; }
</style>
</head>
<body>
<div class="poster">
  <svg viewBox="0 0 601 802" xmlns="http://www.w3.org/2000/svg">
    <defs>
      <linearGradient id="photoTone" x1="0" y1="0" x2="1" y2="1">
        <stop offset="0" stop-color="#8a8f95"/>
        <stop offset="0.45" stop-color="#c9b08a"/>
        <stop offset="0.7" stop-color="#a0826a"/>
        <stop offset="1" stop-color="#5d5f63"/>
      </linearGradient>
    </defs>

    <!-- base -->
    <rect class="canvas-white" width="601" height="802" fill="var(--white)"/>

    <!-- photo area -->
    <polygon class="hero-photo" role="img" aria-label="Foto: Karosseriebauer schleift ein Blechteil, Funkenflug, Schutzvisier"
      points="318,0 601,0 601,450 468,401 160,296" fill="url(#photoTone)"/>

    <!-- blue header shapes -->
    <polygon class="header-blue" points="0,0 298,0 410,62 0,186" fill="var(--brand-blue)"/>
    <polygon class="header-blue-lower" points="0,204 225,296 0,296" fill="var(--brand-blue)"/>

    <!-- dark headline band -->
    <polygon class="headline-band" points="0,296 225,296 468,401 0,401" fill="var(--charcoal)"/>

    <!-- logo -->
    <rect class="logo-mark" x="30" y="46" width="34" height="34" fill="var(--white)"/>
    <text class="display logo-name" x="114" y="58" font-size="18" fill="var(--white)">CARROSSERIE</text>
    <text class="display logo-name" x="114" y="84" font-size="27" fill="var(--white)">LINDAUER + BRACK</text>

    <!-- headlines -->
    <text class="display headline" x="28" y="345" font-size="46" fill="var(--white)" letter-spacing="1">15 RUNDEN</text>
    <text class="display headline" x="28" y="393" font-size="46" fill="var(--white)" letter-spacing="1">SIND ZU FAHREN</text>
    <text class="display subline" x="28" y="446" font-size="45" fill="var(--brand-blue)" letter-spacing="1">DIE SCHNELLSTE ZEIT GEWINNT</text>
    <text class="display intro" x="28" y="483" font-size="32" fill="var(--charcoal)" letter-spacing="1">ZU GEWINNEN GIBT ES</text>

    <!-- prize band -->
    <rect class="prize-band" x="0" y="620" width="601" height="118" fill="var(--brand-blue)"/>

    <!-- prize hexagons -->
    <g stroke="var(--white)" stroke-width="10" stroke-linejoin="round">
      <polygon class="prize-hex" points="106,490 189,536 189,628 106,674 23,628 23,536" fill="var(--brand-blue)"/>
      <polygon class="prize-hex" points="300,490 383,536 383,628 300,674 217,628 217,536" fill="var(--charcoal)"/>
      <polygon class="prize-hex" points="495,490 578,536 578,628 495,674 412,628 412,536" fill="var(--brand-blue)"/>
    </g>

    <g text-anchor="middle" fill="var(--white)">
      <text class="body-text prize-rank" x="106" y="530" font-size="13" font-weight="500" letter-spacing="1">1. PREIS:</text>
      <text class="body-text" x="106" y="559" font-size="18">GUTSCHEIN IM</text>
      <text class="body-text" x="106" y="580" font-size="18">WERT VON</text>
      <text class="display prize-value" x="106" y="612" font-size="32" fill="var(--prize-orange)" letter-spacing="1">CHF 1'000.</text>
      <text class="body-text" x="106" y="631" font-size="12">- VON VANDERMARK</text>

      <text class="body-text prize-rank" x="300" y="530" font-size="13" font-weight="500" letter-spacing="1">2. PREIS:</text>
      <text class="body-text" x="300" y="554" font-size="17">FAHRZEUGREINIGUNG</text>
      <text class="body-text" x="300" y="574" font-size="16">INKL.POLITUR</text>
      <text class="body-text" x="300" y="594" font-size="16">IM WERT VON</text>
      <text class="display prize-value" x="300" y="633" font-size="40" fill="var(--prize-orange)" letter-spacing="1">CHF 800.-</text>

      <text class="body-text prize-rank" x="495" y="540" font-size="13" font-weight="500" letter-spacing="1">3. PREIS:</text>
      <text class="body-text" x="495" y="563" font-size="15">WERKSTATT-GUTSCHEIN</text>
      <text class="body-text" x="495" y="582" font-size="15">IM WERT VON</text>
      <text class="display prize-value" x="495" y="626" font-size="40" fill="var(--prize-orange)" letter-spacing="1">CHF 400.-</text>
    </g>

    <!-- call to action -->
    <polygon class="cta-pill" points="172,688 427,688 443,708 427,728 172,728 156,708" fill="var(--white)"/>
    <text class="display cta-label" x="300" y="716" font-size="21" text-anchor="middle" fill="var(--charcoal)" letter-spacing="1">JETZT MITMACHEN UND GEWINNE</text>

    <!-- footer -->
    <rect class="footer" x="0" y="738" width="601" height="64" fill="var(--charcoal)"/>
    <g fill="none" stroke="var(--white)" stroke-width="1.6">
      <path class="icon-phone" d="M81 763 q-2 2 0 6 q3 5 8 7 q3 1 4 -1 l1 -2 l-3 -2 l-2 1 q-3 -2 -4 -5 l1 -2 l-2 -3 z" fill="var(--white)" stroke="none"/>
      <rect class="icon-mail" x="218" y="764" width="18" height="12" rx="1"/>
      <path d="M218 765 l9 6 l9 -6"/>
      <circle class="icon-web" cx="402" cy="770" r="7"/>
      <ellipse cx="402" cy="770" rx="3" ry="7"/>
      <path d="M395 770 h14"/>
    </g>
    <g class="body-text contact" font-size="13" font-weight="500" fill="var(--white)">
      <text x="106" y="775">+41 32 555 01 87</text>
      <text x="249" y="775">info@lindauer-brack.ch</text>
      <text x="423" y="775">lindauer-brack.ch</text>
    </g>
  </svg>
</div>
</body>
</html>
```